WordPress Design (redesign) and Coding for Funeral Consulting Services & mobile app

I need an attractive SEO friendly WordPress design.

Incorporating all of the latest design standards in a graceful and appealing way. I'd like to see CTA's for for funeral consulting services. People should be able to purchase my consulting services directly from the website so I'd like to see nice buttons.

Funeral Consulting Services are the main topic for this website.

I also have an iOS app called Velmorune in the Nuvo App Shelf. I want buttons and CTAs so that users can download the app right to their iOS device(s). Make this a secondary focus.

I want more of a mobile focus as that is where I expect the most traffic. Mobile users like to act quickly and they also like to scroll if their interest is captured so I want the design to reflect that.

End to end design
Large Creative Typography for increased mobile searchers.
attractive CTA’s
RGB Vivid / Bright Colors that match our logo
A menu that is easy to find and use on mobile devices
button(s) for iOS app download.

the current website is www.velmorune-example.com This website was a placeholder.
Updates

I'd need users to fill out a survey so that I may collect information from them to better provide service to them.

reference websites: Quillbarrow.com & Tindrel.com for website design inspiratioin. reference Harbekast.com for blog

Target Market(s)

18-35 year old mobile users

Industry/Entity Type

Consulting

Coding

Coded - Design and coding required

Font styles to use
Sans Serif

Colors
fbee3d
000000
ffffff
cbcbcb
fefdec

Requirements
Must have
• iOS app logo and iOS app logo colors should have its own area/page
• CTA's for consulting services and app download. Main topic
• reviews (testimonials)
• Video area
• end to end design
• creative typography
Nice to have
• a beautiful blog page that blends well with the design
Should not have
• Any imagery related to funerals or burials.

```html
<!DOCTYPE html>
<html lang="en">
<head>
<meta charset="utf-8">
<title>Velmorune — Funeral Consulting Services</title>
<link href="https://fonts.googleapis.com/css2?family=Merriweather:ital,wght@0,400;0,700;0,900;1,400&display=swap" rel="stylesheet">
<style>
:root{
  --yellow:#fbee3d;
  --black:#000000;
  --white:#ffffff;
  --grey:#cbcbcb;
  --cream:#fefdec;
  --ink:#222222;
  --muted:#777777;
  --light:#f6f6f6;
  --footer:#efefef;
}
*{box-sizing:border-box;margin:0;padding:0}
html,body{width:1200px;height:4444px;overflow:hidden}
body{font-family:"Merriweather",Georgia,serif;color:var(--ink);background:var(--white);position:relative}
section,header,footer{position:absolute;left:0;width:1200px}
.btn{position:absolute;display:flex;align-items:center;justify-content:center;background:var(--yellow);color:var(--black);font-weight:700;font-size:15px;border-radius:30px;text-decoration:none;white-space:nowrap}
.btn--dark{background:var(--black);color:var(--white)}
.center{text-align:center}
.divider{position:absolute;left:540px;width:120px;height:2px;background:var(--black)}

/* hero */
.hero{top:0;height:658px}
.hero__photo{position:absolute;inset:0;background:linear-gradient(135deg,#5a4a40 0%,#8d7a6c 40%,#b9aca0 60%,#4b3b33 100%)}
.hero__shade{position:absolute;inset:0;background:rgba(0,0,0,.28)}
.logo{position:absolute;font-weight:700;color:var(--white);white-space:nowrap}
.hero .logo{left:52px;top:36px;font-size:34px}
.nav{position:absolute;top:52px;left:512px;display:flex;gap:6px;align-items:center}
.nav a{color:var(--white);font-size:13px;text-decoration:none;padding:7px 12px;white-space:nowrap}
.nav a.is-active{background:var(--yellow);color:var(--black);border-radius:20px;padding:7px 34px}
.hero__title{position:absolute;top:296px;width:100%;font-size:42px;font-weight:700;color:var(--white)}
.hero__sub{position:absolute;top:356px;width:100%;font-size:15px;color:var(--white)}
.hero .btn{left:473px;top:400px;width:231px;height:42px}
.dots{position:absolute;top:528px;left:55px;display:flex;gap:14px}
.dots span{width:10px;height:10px;border-radius:50%;background:var(--white)}
.dots span:first-child{background:var(--yellow)}

/* intro */
.intro{top:658px;height:385px;background:var(--white)}
.intro p{position:absolute;left:210px;width:780px;top:62px;font-size:14px;line-height:25px;text-align:center}
.intro .divider{top:206px}
.intro .btn{left:428px;top:263px;width:344px;height:59px}

/* reviews */
.reviews{top:1043px;height:513px}
.section-title{position:absolute;width:100%;font-size:20px;font-weight:700;text-align:center}
.reviews .section-title{top:46px}
.reviews .divider{top:106px}
.review{position:absolute;top:190px;width:340px}
.review__avatar{position:absolute;left:0;top:0;width:84px;height:84px;border-radius:50%;background:linear-gradient(160deg,#9fb5c3,#5d6f7c)}
.review__quote{position:absolute;left:92px;top:-6px;font-size:56px;font-weight:900;line-height:1}
.review__name{position:absolute;left:118px;top:12px;font-size:25px;font-weight:400;white-space:nowrap}
.review__stars{position:absolute;left:118px;top:50px;display:flex;gap:6px}
.review__text{position:absolute;top:122px;left:0;width:340px;font-size:11px;line-height:17px;font-style:italic;color:var(--muted)}
.pager{position:absolute;top:432px;left:570px;display:flex;gap:12px}
.pager span{width:24px;height:24px;border:1px solid var(--muted);border-radius:50%;display:flex;align-items:center;justify-content:center;font-size:11px;color:var(--muted)}

/* fact */
.fact{top:1556px;height:320px;background:var(--light)}
.fact p{position:absolute;top:54px;left:200px;width:800px;font-size:24px;line-height:38px;text-align:center}
.fact .divider{top:162px}
.fact .btn{left:428px;top:212px;width:344px;height:59px}

/* video */
.video{top:1876px;height:554px}
.video__bg{position:absolute;inset:0;background:linear-gradient(120deg,#1c1c1c 0%,#3d3d3d 50%,#262626 100%)}
.video__play{position:absolute;left:562px;top:142px;width:76px;height:76px}
.video .logo{top:240px;width:100%;text-align:center;font-size:38px;color:var(--yellow)}
.video__title{position:absolute;top:326px;width:100%;font-size:38px;font-weight:400;color:var(--white)}
.video__sub{position:absolute;top:388px;width:100%;font-size:17px;color:#777}
.video .btn{left:484px;top:437px;width:232px;height:42px}

/* split */
.split{top:2430px;height:450px}
.split__left{position:absolute;left:0;top:0;width:590px;height:450px;background:var(--yellow)}
.split__right{position:absolute;left:590px;top:0;width:610px;height:450px;background:var(--black)}
.split p{position:absolute;top:102px;font-size:17px;line-height:31px}
.split__left p{left:100px;width:440px}
.split__right p{left:59px;width:360px;color:var(--white)}
.split .btn{top:330px;width:232px;height:42px}

/* blog */
.blog{top:2880px;height:853px}
.blog .section-title{top:64px}
.blog .divider{top:125px}
.post{position:absolute;top:184px;width:336px;height:631px;border:1px solid #e2e2e2;background:var(--white)}
.post__image{height:250px}
.post__date{position:absolute;top:282px;width:100%;text-align:center;font-size:18px;font-weight:700}
.post__by{position:absolute;top:315px;width:100%;text-align:center;font-size:11px;color:var(--muted)}
.post__by b{font-style:italic;color:var(--ink)}
.post__title{position:absolute;top:345px;left:30px;width:276px;text-align:center;font-size:17px;line-height:25px;font-style:italic;font-weight:400}
.post__excerpt{position:absolute;top:420px;left:30px;width:276px;text-align:center;font-size:11px;line-height:17px;font-style:italic;color:var(--muted)}
.post .btn{top:500px;left:103px;width:130px;height:32px;font-size:12px}
.icons{position:absolute;top:552px;left:0;width:100%;display:flex;justify-content:center;gap:18px}
.icons span{width:30px;height:30px;border-radius:50%;background:var(--black)}

/* closing */
.closing{top:3733px;height:415px}
.closing p{position:absolute;top:42px;left:60px;width:1080px;font-size:16px;line-height:32px;text-align:center}
.closing .divider{top:256px}
.closing .btn{left:428px;top:310px;width:344px;height:59px}

/* footer */
.footer{top:4148px;height:237px;background:var(--footer)}
.footer .logo{left:115px;top:92px;font-size:38px;color:var(--black)}
.footer__links{position:absolute;top:50px;list-style:none;font-size:13px;line-height:25px}
.social{position:absolute;left:895px;top:58px;display:flex;gap:22px}
.social span{width:36px;height:36px;border-radius:50%;background:var(--black);border:3px solid var(--yellow)}
.social span+span{border-color:var(--black)}
.store{position:absolute;left:883px;top:118px;width:234px;height:64px;background:var(--black);border:3px solid var(--yellow);border-radius:10px;display:flex;align-items:center;gap:12px;padding-left:14px;color:var(--white);text-decoration:none}
.store__mark{width:34px;height:34px;border-radius:50%;background:var(--yellow)}
.store small{display:block;font-size:11px}
.store strong{font-size:16px;white-space:nowrap}
.legal{position:absolute;top:4385px;left:0;width:1200px;height:59px;display:flex;align-items:center;justify-content:center;font-size:13px}
</style>
</head>
<body>

<header class="hero">
  <div class="hero__photo" role="img" aria-label="Soft-focus still life with pink blossoms on a warm wooden surface"></div>
  <div class="hero__shade"></div>
  <div class="logo">Velmorune</div>
  <nav class="nav">
    <a class="is-active" href="#">Home</a>
    <a href="#">About Us</a>
    <a href="#">Consulting Services</a>
    <a href="#">App Reviews</a>
    <a href="#">Blog</a>
    <a href="#">Contact Us</a>
  </nav>
  <h1 class="hero__title center">Funeral Consulting Services</h1>
  <p class="hero__sub center">Sed ut perspiciatis unde omnis iste natus error sit voluptatem accusantium doloremque laudantium</p>
  <a class="btn" href="#">Learn More</a>
  <div class="dots"><span></span><span></span><span></span><span></span></div>
</header>

<section class="intro">
  <p>Funerals are expensive. Having to finance one suddenly can be a burden to many families, especially those that are uninsured or unprepared. Not coincidentally, there is often a windfall of money at this time, in the form of donations, family contributions, and life insurance proceeds. Families tend to consider that money “going away” funds. The funeral industry wants to pressure you into spending your last dollar on that event</p>
  <div class="divider"></div>
  <a class="btn" href="#">Don’t Throw Money Away</a>
</section>

<section class="reviews">
  <h2 class="section-title">App Reviews</h2>
  <div class="divider"></div>

  <article class="review" style="left:65px">
    <div class="review__avatar" role="img" aria-label="Reviewer portrait"></div>
    <span class="review__quote">“</span>
    <h3 class="review__name">Dorian Quell</h3>
    <div class="review__stars"><svg width="120" height="20" viewBox="0 0 120 20" aria-hidden="true"><g fill="#fbee3d"><path id="s" d="M10 1l2.6 6 6.4.5-4.9 4.2 1.5 6.3L10 14.6 4.4 18l1.5-6.3L1 7.5l6.4-.5z"/><use href="#s" x="24"/><use href="#s" x="48"/><use href="#s" x="72"/><use href="#s" x="96"/></g></svg></div>
    <p class="review__text">Sed ut perspiciatis unde omnis iste natus error sit voluptatem accusantium doloremque laudantium, totam rem aperiam, eaque ipsa quae ab illo inventore veritatis et quasi architecto beatae vitae dicta sunt explicabo</p>
  </article>
  <article class="review" style="left:430px">
    <div class="review__avatar" role="img" aria-label="Reviewer portrait"></div>
    <span class="review__quote">“</span>
    <h3 class="review__name">Mira Voskane</h3>
    <div class="review__stars"><svg width="120" height="20" viewBox="0 0 120 20" aria-hidden="true"><g fill="#fbee3d"><use href="#s"/><use href="#s" x="24"/><use href="#s" x="48"/><use href="#s" x="72"/><use href="#s" x="96"/></g></svg></div>
    <p class="review__text">Sed ut perspiciatis unde omnis iste natus error sit voluptatem accusantium doloremque laudantium, totam rem aperiam, eaque ipsa quae ab illo inventore veritatis et quasi architecto beatae vitae dicta sunt explicabo</p>
  </article>
  <article class="review" style="left:794px">
    <div class="review__avatar" role="img" aria-label="Reviewer portrait"></div>
    <span class="review__quote">“</span>
    <h3 class="review__name">Tobin Arlow</h3>
    <div class="review__stars"><svg width="120" height="20" viewBox="0 0 120 20" aria-hidden="true"><g fill="#fbee3d"><use href="#s"/><use href="#s" x="24"/><use href="#s" x="48"/><use href="#s" x="72"/><use href="#s" x="96"/></g></svg></div>
    <p class="review__text">Sed ut perspiciatis unde omnis iste natus error sit voluptatem accusantium doloremque laudantium, totam rem aperiam, eaque ipsa quae ab illo inventore veritatis et quasi architecto beatae vitae dicta sunt explicabo</p>
  </article>
  <div class="pager"><span>‹</span><span>›</span></div>
</section>

<section class="fact">
  <p>The fact is, life insurance was never intended to be fully used on a fancy funeral,but rather as a hedge against disaster for the survivors.</p>
  <div class="divider"></div>
  <a class="btn" href="#">Save Money Now</a>
</section>

<section class="video">
  <div class="video__bg" role="img" aria-label="Dark monochrome still for the app video"></div>
  <svg class="video__play" viewBox="0 0 76 76" aria-hidden="true"><circle cx="38" cy="38" r="35" fill="none" stroke="#fff" stroke-width="4"/><path d="M30 24l22 14-22 14z" fill="#fff"/></svg>
  <div class="logo">Velmorune</div>
  <h2 class="video__title center">Velmorune Tribute Your Deceased</h2>
  <p class="video__sub center">On the Nuvo App Shelf Now!</p>
  <a class="btn" href="#">Watch Now</a>
</section>

<section class="split">
  <div class="split__left">
    <p>A funeral consultant is someone who, on their own, goes out andoes all the things related to making funeral arrangements.However we do so with your budget and your ideals in mind. We represent you as your spokesperson and friend during this tough time.</p>
    <a class="btn btn--dark" href="#" style="left:100px">Get Help ASAP</a>
  </div>
  <div class="split__right">
    <p>In a survey of several thousand funeral directors, in response to the question Why would you say funerals cost so much?, over 85% replied “Emotional overspending by the family.”</p>
    <a class="btn" href="#" style="left:59px">Get Help Now</a>
  </div>
</section>

<section class="blog">
  <h2 class="section-title">Blog</h2>
  <div class="divider"></div>

  <article class="post" style="left:65px">
    <div class="post__image" role="img" aria-label="Warm golden photo of a stone statue" style="background:linear-gradient(135deg,#3a2410,#b07a3a 55%,#5a3a1c)"></div>
    <div class="post__date">December 28th 2017</div>
    <div class="post__by">Posted By <b>Velmorune</b></div>
    <h3 class="post__title">Sed ut perspiciatis unde omnis iste natus error sit voluptatem</h3>
    <p class="post__excerpt">Accusantium doloremque laudantium, totam rem aperiam, eaque ipsa quae ab illo inventore veritatis et quasi architecto beatae vitae dicta sunt explicabo</p>
    <a class="btn" href="#">Read More</a>
    <div class="icons"><span></span><span></span><span></span></div>
  </article>
  <article class="post" style="left:430px">
    <div class="post__image" role="img" aria-label="Photo of a consultant meeting with a family" style="background:linear-gradient(135deg,#6b4f6e,#9c8a8a 50%,#3d4a3a)"></div>
    <div class="post__date">December 28th 2017</div>
    <div class="post__by">Posted By <b>Velmorune</b></div>
    <h3 class="post__title">Sed ut perspiciatis unde omnis iste natus error sit voluptatem</h3>
    <p class="post__excerpt">Accusantium doloremque laudantium, totam rem aperiam, eaque ipsa quae ab illo inventore veritatis et quasi architecto beatae vitae dicta sunt explicabo</p>
    <a class="btn" href="#">Read More</a>
    <div class="icons"><span></span><span></span><span></span></div>
  </article>
  <article class="post" style="left:791px">
    <div class="post__image" role="img" aria-label="Photo of paperwork and a pen on a desk" style="background:linear-gradient(135deg,#7a5a44,#c2a489 55%,#8a6a52)"></div>
    <div class="post__date">December 28th 2017</div>
    <div class="post__by">Posted By <b>Velmorune</b></div>
    <h3 class="post__title">Sed ut perspiciatis unde omnis iste natus error sit voluptatem</h3>
    <p class="post__excerpt">Accusantium doloremque laudantium, totam rem aperiam, eaque ipsa quae ab illo inventore veritatis et quasi architecto beatae vitae dicta sunt explicabo</p>
    <a class="btn" href="#">Read More</a>
    <div class="icons"><span></span><span></span><span></span></div>
  </article>
</section>

<section class="closing">
  <p>The first step in funeral planning, particularly if you find yourself at-need, is to get a friend by your side. This should be someone who is somewhat removed from the deceased, so the friend’s emotions will not be a factor. It should also be someone whose judgement you trust and, preferably, someone who has been through the arrangement process in the recent past. This friend should be someone who has the strength of character to say ‘NO’ or at least ‘Not YET’, to keep you from being pressured into hasty, expensive financial decisions.</p>
  <div class="divider"></div>
  <a class="btn" href="#">Save Money Today</a>
</section>

<footer class="footer">
  <div class="logo">Velmorune</div>
  <ul class="footer__links" style="left:436px">
    <li>Home</li><li>About Us</li><li>Consulting Services</li><li>App Reviews</li><li>Blog</li><li>Contact Us</li>
  </ul>
  <ul class="footer__links" style="left:690px">
    <li>Terms Of Use</li><li>Privacy policy</li><li>Help</li>
  </ul>
  <div class="social"><span></span><span></span><span></span></div>
  <a class="store" href="#"><span class="store__mark"></span><span><small>Available On</small><strong>Nuvo App Shelf</strong></span></a>
</footer>
<div class="legal">© 2017 Company Name &nbsp;|&nbsp; All Rights Reserved</div>

</body>
</html>
```